Fairbrook's Vacation Rentals Business Card

Multi Million dollar villa rentals in the Dominican Republic.

Industry/Entity Type

Business

Contact Information for Business Card

I am looking for a high-end look around my company name/logo (see attached) on one side incorporating the following info: first and last name, title, address, phone #, email and company website. On the backside I want to add a full color picture of one of our villas (see attached).

```html
<!DOCTYPE html>
<html lang="en">
<head>
<meta charset="utf-8">
<title>Fairbrook's Vacation Rentals – Business Card</title>
<link href="https://fonts.googleapis.com/css2?family=Arimo:wght@400;700&display=swap" rel="stylesheet">
<style>
  :root {
    --backdrop: #3a3a3a;
    --card-orange: #fbb03b;
    --card-orange-light: #fdc35a;
    --card-orange-deep: #f7a52a;
    --ink: #1a1a1a;
    --paper: #ffffff;
    --accent-red: #ef4a3a;
    --sky: #3f8fd8;
    --villa-white: #eeeae2;
    --pool: #1fa6e0;
  }
  * { box-sizing: border-box; margin: 0; padding: 0; }
  html, body {
    width: 1200px; height: 800px; overflow: hidden;
    background: var(--backdrop);
    font-family: 'Arimo', Arial, sans-serif;
  }
  .canvas { position: relative; width: 1200px; height: 800px; }
  .card {
    position: absolute; top: 234px;
    width: 548px; height: 331px;
    border-radius: 22px; overflow: hidden;
  }
  .card--back { left: 36px; }
  .villa-photo {
    width: 100%; height: 100%;
    background: linear-gradient(180deg, var(--sky) 0%, #8cc4ea 18%, var(--villa-white) 35%, #d9d2c4 62%, #cfcac0 76%, var(--pool) 84%, #0f8fd0 100%);
  }
  .card--front {
    left: 617px;
    background: radial-gradient(ellipse at 45% 55%, var(--card-orange-light) 0%, var(--card-orange) 55%, var(--card-orange-deep) 100%);
    color: var(--ink);
  }
  .brand {
    position: absolute; left: 30px; top: 140px;
    display: flex; align-items: center; gap: 8px;
  }
  .brand__dot { width: 14px; height: 14px; border-radius: 50%; background: var(--ink); }
  .brand__name { font-size: 17px; font-weight: 700; color: var(--ink); line-height: 1.2; }
  .divider {
    position: absolute; left: 269px; top: 54px;
    width: 2px; height: 228px; background: var(--ink);
  }
  .details { position: absolute; left: 285px; top: 0; width: 250px; }
  .person__name { position: absolute; top: 62px; font-size: 18px; white-space: nowrap; }
  .person__title {
    position: absolute; top: 82px; display: flex; align-items: center; gap: 4px;
  }
  .person__title span {
    background: var(--ink); color: var(--card-orange-light);
    font-size: 17px; padding: 0 4px; line-height: 21px;
  }
  .contact { position: absolute; display: flex; align-items: center; gap: 5px; font-size: 15.5px; white-space: nowrap; }
  .contact svg { width: 18px; height: 18px; flex: none; }
  .contact--phone { top: 130px; }
  .contact--email { top: 155px; }
  .address { position: absolute; top: 209px; font-size: 15.5px; line-height: 20px; }
  .website {
    position: absolute; top: 255px;
    font-size: 17px; padding: 0 8px 0 2px;
    background: linear-gradient(180deg, transparent 0%, var(--accent-red) 0%, var(--accent-red) 100%);
    text-decoration: underline;
  }
</style>
</head>
<body>
<div class="canvas">
  <section class="card card--back">
    <div class="villa-photo" role="img" aria-label="Photograph of a white two-storey villa with a terracotta roof, arched veranda, blue loungers and a swimming pool"></div>
  </section>

  <section class="card card--front">
    <div class="brand">
      <div class="brand__dot"></div>
      <div class="brand__name">Fairbrook's<br>Vacation Rentals</div>
    </div>
    <div class="divider"></div>
    <div class="details">
      <div class="person__name">RAY T. HALVORSEN</div>
      <div class="person__title">
        <span>Co-Ordinator</span>
        <svg width="26" height="20" viewBox="0 0 26 20"><path d="M6 2h5l-6 16H0z M17 2h5l-6 16h-5z" fill="#1a1a1a"/></svg>
      </div>
      <div class="contact contact--phone">
        <svg viewBox="0 0 18 18"><rect width="18" height="18" rx="2" fill="#1a1a1a"/><path d="M5 4c1 0 2 2 2 3l-1 1c1 2 2 3 4 4l1-1c1 0 3 1 3 2l-1 2C8 15 3 10 3 5z" fill="#fbb03b"/></svg>
        512-555-0143
      </div>
      <div class="contact contact--email">
        <svg viewBox="0 0 18 18"><rect width="18" height="18" rx="2" fill="#1a1a1a"/><rect x="3.5" y="5" width="11" height="8" fill="none" stroke="#fbb03b" stroke-width="1.3"/><path d="M3.5 5l5.5 4.5 5.5-4.5" fill="none" stroke="#fbb03b" stroke-width="1.3"/></svg>
        RayTHalvorsen@tidepost.us
      </div>
      <div class="address">1475 Marlow Lane<br>Brenton, TX 76501</div>
      <div class="website">www.website.com</div>
    </div>
  </section>
</div>
</body>
</html>
```